Vorlund Business Card Design Needed

We are a consultation firm called "Vorlund Inc" or simply Vorlund. Would would like a simple card utilizing the blue and grays in our logo (perhaps even different shades and hues of blue). Logo and Initials of Card holder one side and information on the other.

Target Market(s)

We are B 2 B company. We deal mostly with upper management.

Industry/Entity Type

Business

Contact Information for Business Card

Name. Title. phone. email. website.

```html
<!DOCTYPE html>
<html lang="en">
<head>
<meta charset="utf-8">
<title>Vorlund Inc Business Card</title>
<link rel="stylesheet" href="https://fonts.googleapis.com/css2?family=Open+Sans:ital,wght@0,300;0,400;0,600;1,400&display=swap">
<style>
  :root {
    --bg: #eeeef3;
    --card: #ffffff;
    --navy: #1c4a7a;
    --blue: #1f86cf;
    --cyan: #2bb3d6;
    --deep: #0f4a82;
    --grey: #c9cacc;
    --grey-text: #9a9ca0;
    --ink: #4a4c50;
    --rule: #8e9094;
  }
  * { margin: 0; padding: 0; box-sizing: border-box; }
  html, body {
    width: 1200px; height: 900px; overflow: hidden;
    background: var(--bg);
    font-family: "Open Sans", Arial, sans-serif;
  }
  .stage {
    width: 1200px; height: 900px;
    display: flex; align-items: center; justify-content: center; gap: 40px;
  }
  .card {
    position: relative;
    width: 540px; height: 309px;
    background: var(--card);
    border-radius: 24px;
    overflow: hidden;
    box-shadow: 0 6px 18px rgba(40, 50, 80, 0.12);
  }
  /* info side */
  .holder {
    position: absolute; left: 38px; top: 44px;
  }
  .holder-name {
    font-size: 22px; font-weight: 600; color: var(--navy); line-height: 1.1;
  }
  .holder-title {
    font-size: 11px; font-weight: 300; color: var(--grey-text); margin-top: 3px;
  }
  .contact-list { list-style: none; margin-top: 14px; }
  .contact-list li {
    display: flex; align-items: center; gap: 8px;
    font-size: 14px; color: var(--ink); line-height: 1.6;
  }
  .contact-list svg { width: 13px; height: 13px; flex: none; }
  .divider {
    position: absolute; left: 38px; right: 38px; top: 158px;
    border-top: 1px solid var(--rule);
  }
  .brand {
    position: absolute; display: flex; align-items: center; gap: 10px;
  }
  .brand-dot {
    width: 18px; height: 18px; border-radius: 50%; background: var(--blue);
  }
  .brand-name {
    font-size: 30px; font-weight: 600; color: var(--blue); line-height: 1;
  }
  .card-info .brand { right: 40px; top: 80px; }
  .band { position: absolute; inset: 0; width: 100%; height: 100%; }
  .band-url {
    position: absolute; right: 34px; bottom: 12px;
    font-size: 15px; color: #ffffff; letter-spacing: 0.3px;
    transform: rotate(5.8deg); transform-origin: right bottom;
  }
  /* logo side */
  .card-logo .brand-block {
    position: absolute; inset: 0;
    display: flex; flex-direction: column; align-items: center; justify-content: center; gap: 16px;
  }
  .card-logo .brand { position: static; }
  .logo-url {
    font-size: 13px; font-style: italic; color: var(--blue);
  }
</style>
</head>
<body>
<main class="stage">
  <section class="card card-info" aria-label="Information side">
    <svg class="band" viewBox="0 0 540 309" preserveAspectRatio="none" aria-hidden="true">
      <defs>
        <linearGradient id="bandFill" x1="0" y1="0" x2="1" y2="0">
          <stop offset="0" stop-color="#2bb3d6"/>
          <stop offset="0.5" stop-color="#1a86b8"/>
          <stop offset="1" stop-color="#0f4a82"/>
        </linearGradient>
      </defs>
      <polygon points="0,206 540,262 540,270 0,214" fill="#c9cacc"/>
      <polygon points="0,216 540,272 540,309 0,309" fill="url(#bandFill)"/>
    </svg>

    <div class="holder">
      <h1 class="holder-name">Daniel Ostrava</h1>
      <p class="holder-title">Senior Vice President</p>
      <ul class="contact-list">
        <li>
          <svg viewBox="0 0 12 12" aria-hidden="true"><rect x="2.5" y="0.5" width="7" height="11" rx="1.2" fill="none" stroke="#4a4c50"/><line x1="5" y1="9.5" x2="7" y2="9.5" stroke="#4a4c50"/></svg>
          0170-555-0142
        </li>
        <li>
          <svg viewBox="0 0 12 12" aria-hidden="true"><rect x="0.5" y="2" width="11" height="8" fill="none" stroke="#4a4c50"/><polyline points="0.5,2 6,6.5 11.5,2" fill="none" stroke="#4a4c50"/></svg>
          info@ostrava.de
        </li>
      </ul>
    </div>
    <div class="divider"></div>

    <div class="brand">
      <span class="brand-dot"></span>
      <span class="brand-name">Vorlund</span>
    </div>

    <p class="band-url">www.VorlundInc.com</p>
  </section>

  <section class="card card-logo" aria-label="Logo side">
    <div class="brand-block">
      <div class="brand">
        <span class="brand-dot"></span>
        <span class="brand-name">Vorlund</span>
      </div>
      <p class="logo-url">www.VorlundInc.com</p>
    </div>
  </section>
</main>
</body>
</html>
```